"Tidelark Ministry" needs a logo design that represents a Christian family boating ministry

Mission Statement:
“Providing compassion, care and opportunities to create memories for marginalized groups of society through ocean therapy.”
Bible verse:
Colossians 3:12 – “Therefore, as God’s chosen people, holy and dearly loved, clothe yourselves with compassion, kindness, humility, gentleness and patience.”
Target Market(s)
HOMELESS (who have gone through shelters and are on the road to recovery)
CHURCH GROUPS
INJURED MILITARY VETERANS
YOUTH AT RISK (orphans, human trafficking survivors)
SICKLY (hospitalized who can get out once in a while)
CAREGIVERS (single moms, military spouses caring for injured vets, families of those in prison)
ELDERLY (retirement centers)
SMALL BUSINESS STAFF OUTINGS
SPECIAL EVENTS
Industry/Entity Type
Ministry
Contact Information for Business Card
Captain Glen Marbury @ 555-014-2931
Priscilla Marbury @ 555-018-6457
info@tidelarkministry-example.com
www.tidelarkministry-example.com (not active yet but hopefully, soon)
Requirements
Must have
- Catch-phrase words maybe for back of business card:
- "Tidelark --- Kindness --- Sharing days on the waves"
Nice to have
- Added 2 photo files just for visuals:
- 1 photo is of our boat.
- Other photo is our daughter's artwork on a cooler she made (for father's day gift)...might be nice and fun to incorporate daughter's artwork/inspiration into logo...but not sure if it looks to busy

```html
<!DOCTYPE html>
<html lang="en">
<head>
<meta charset="utf-8">
<title>Tidelark Ministry — Business Card</title>
<link href="https://fonts.googleapis.com/css2?family=Lato:ital,wght@0,400;0,700;1,400&family=Mulish:wght@700&display=swap" rel="stylesheet">
<style>
  :root {
    --stage: #0a0a0a;
    --card-white: #ffffff;
    --navy: #1f3b60;
    --band: #30527a;
    --accent-red: #e0262a;
    --on-dark: #ffffff;
  }
  * { margin: 0; padding: 0; box-sizing: border-box; }
  html, body { width: 1200px; height: 900px; overflow: hidden; }
  body { background: var(--stage); position: relative; font-family: "Lato", sans-serif; }

  .card {
    position: absolute;
    top: 306px;
    width: 439px;
    height: 271px;
    border-radius: 11px;
    overflow: hidden;
    box-shadow: 0 3px 8px rgba(0,0,0,0.5);
  }

  .brand-mark { position: absolute; border-radius: 50%; }

  /* Front */
  .card-front { left: 149px; background: var(--card-white); }
  .people { position: absolute; left: 23px; top: 22px; color: var(--navy); font-weight: 700; font-size: 14.5px; line-height: 22px; }
  .card-front .brand-mark { left: 286px; top: 62px; width: 58px; height: 58px; background: var(--navy); }
  .brand-name {
    position: absolute; right: 23px; top: 125px;
    font-family: "Mulish", sans-serif; font-weight: 700; font-size: 21px;
    color: var(--navy); letter-spacing: 0.7px;
  }
  .contacts { position: absolute; left: 22px; top: 143px; list-style: none; color: var(--navy); font-size: 12.5px; }
  .contacts li { display: flex; align-items: center; height: 17px; }
  .contacts svg { width: 10px; height: 10px; margin-right: 6px; fill: var(--accent-red); flex: none; }
  .verse-band {
    position: absolute; left: 0; right: 0; bottom: 0; height: 60px;
    background: var(--band); color: var(--on-dark);
    display: flex; align-items: center; justify-content: center; text-align: center;
    font-style: italic; font-size: 11px; line-height: 14px; padding: 0 30px;
  }

  /* Back */
  .card-back { left: 608px; background: var(--band); color: var(--on-dark); text-align: center; }
  .card-back .brand-mark { left: 180px; top: 66px; width: 82px; height: 82px; background: var(--on-dark); }
  .back-name {
    position: absolute; left: 0; right: 0; top: 158px;
    font-family: "Mulish", sans-serif; font-weight: 700; font-size: 33px; letter-spacing: 1px;
  }
  .tagline { position: absolute; left: 0; right: 0; top: 229px; font-size: 13.5px; }
</style>
</head>
<body>

  <section class="card card-front" aria-label="Business card front">
    <div class="people">
      <p>Captain Glen Marbury</p>
      <p>First Mate Priscilla Marbury</p>
    </div>

    <div class="brand-mark" role="img" aria-label="Ministry brand mark"></div>
    <p class="brand-name">Tidelark Ministry</p>

    <ul class="contacts">
      <li>
        <svg viewBox="0 0 10 10" aria-hidden="true"><path d="M2.2 0.6l1.6 1.8-0.9 1.2c0.6 1.3 1.6 2.3 2.9 2.9l1.2-0.9 1.8 1.6-0.9 1.6C5 9 1 5 0.6 1.5z"/></svg>
        555-018-6457
      </li>
      <li>
        <svg viewBox="0 0 10 10" aria-hidden="true"><rect x="0.5" y="2" width="9" height="6"/><path d="M0.5 2l4.5 3.5 4.5-3.5" stroke="#fff" stroke-width="0.8" fill="none"/></svg>
        info@tidelarkministry-example.com
      </li>
      <li>
        <svg viewBox="0 0 10 10" aria-hidden="true"><circle cx="5" cy="5" r="4.6"/><path d="M0.6 5h8.8M5 0.4c-2 2.6-2 6.6 0 9.2M5 0.4c2 2.6 2 6.6 0 9.2" stroke="#fff" stroke-width="0.7" fill="none"/></svg>
        www.tidelarkministry-example.com
      </li>
    </ul>

    <p class="verse-band">Therefore, as God’s chosen people, holy and dearly loved, clothe yourselves with compassion, kindness, humility, gentleness and patience. - Colossians 3:12</p>
  </section>

  <section class="card card-back" aria-label="Business card back">
    <div class="brand-mark" role="img" aria-label="Ministry brand mark"></div>
    <p class="back-name">Tidelark Ministry</p>
    <p class="tagline">Tidelark | Kindness | Sharing Days On The Waves</p>
  </section>

</body>
</html>
```